Label design/Graphic design required to brand wall paints

Would like to design a paint drum label/graphic to brand paint drums. The product is wall paints which come in plastic containers. (Refer attached pics). I have also attached the logo font. The one in the pictures are a bit too plan - need some color and creativity - not something too jazzy. You can change the icons if you wish to for the Low VOC, Washable & Eco Friendly - or keep the same. Need to incorporate the drum size "20 L" or "20 Ltr." at the bottom of the label.Rest of the matter to be incorporated is as per the content in the sample labels provided. Size of the label can be 230 x 230mm W X H.

Target Market(s)

Buildings Houses

Industry/Entity Type

Painting And Decorating

Colors

Designer to choose colors to be used in the design.

Requirements
Must have
• The content on the label samples given. Must maintain the logo font.
Nice to have
• A little more color -not jazzy. Can try giving color accents to the font if it helps.
Should not have
• Should not be cluttered.

```html
<!DOCTYPE html>
<html lang="en">
<head>
<meta charset="utf-8">
<title>Orvessa Paints – 20 L Drum Label</title>
<link rel="stylesheet" href="https://fonts.googleapis.com/css2?family=Poiret+One&family=Open+Sans:wght@400;600&display=swap">
<style>
  :root {
    --backdrop: #808080;
    --label: #ffffff;
    --ink: #1b1b1b;
    --ink-soft: #333333;
    --icon-green: #1e9b48;
    --icon-blue: #2a5cc7;
    --icon-sky: #7fb8e6;
  }
  html, body {
    margin: 0;
    width: 1200px;
    height: 1000px;
    overflow: hidden;
    background: var(--backdrop);
  }
  .label-art {
    display: block;
    width: 1200px;
    height: 1000px;
  }
  .brand-name {
    font-family: "Poiret One", sans-serif;
    font-size: 138px;
    fill: var(--label);
    stroke: var(--label);
    stroke-width: 1px;
  }
  .product-title {
    font-family: "Poiret One", sans-serif;
    font-size: 215px;
    fill: var(--ink);
    stroke: var(--ink);
    stroke-width: 2px;
  }
  .product-sub {
    font-family: "Poiret One", sans-serif;
    font-size: 72px;
    fill: var(--ink);
    stroke: var(--ink);
    stroke-width: 1px;
  }
  .feature-caption {
    font-family: "Open Sans", sans-serif;
    font-size: 18px;
    fill: var(--ink-soft);
  }
  .volume {
    font-family: "Open Sans", sans-serif;
    font-weight: 600;
    font-size: 38px;
    fill: var(--label);
  }
  .tagline {
    font-family: "Open Sans", sans-serif;
    font-size: 27px;
    fill: var(--ink);
  }
</style>
</head>
<body>
<svg class="label-art" viewBox="0 0 1200 1000" xmlns="http://www.w3.org/2000/svg">
  <defs>
    <linearGradient id="spectrum" x1="0" y1="0" x2="1" y2="0">
      <stop offset="0" stop-color="#ff1493"/>
      <stop offset="0.25" stop-color="#7a10d6"/>
      <stop offset="0.45" stop-color="#00a6e6"/>
      <stop offset="0.65" stop-color="#2fc21a"/>
      <stop offset="0.8" stop-color="#e5e60a"/>
      <stop offset="1" stop-color="#ff1a00"/>
    </linearGradient>
  </defs>

  <rect class="label-sheet" x="168" y="87" width="845" height="843" fill="var(--label)"/>

  <path class="header-band" d="M168 240 H1013 V302 Q1013 352 963 352 H218 Q168 352 168 302 Z" fill="url(#spectrum)"/>
  <path class="header" d="M168 87 H1013 V268 Q1013 318 963 318 H218 Q168 318 168 268 Z" fill="var(--ink)"/>
  <text class="brand-name" x="590" y="255" text-anchor="middle" textLength="710" lengthAdjust="spacingAndGlyphs">ORVESSA</text>

  <text class="product-title" x="590" y="557" text-anchor="middle" textLength="710" lengthAdjust="spacingAndGlyphs">PAINTS</text>
  <text class="product-sub" x="588" y="652" text-anchor="middle" textLength="565" lengthAdjust="spacingAndGlyphs">PAINT + PRIMER</text>

  <rect x="312" y="688" width="6" height="82" rx="3" fill="var(--ink-soft)"/>
  <rect x="863" y="688" width="6" height="82" rx="3" fill="var(--ink-soft)"/>

  <g class="feature low-voc">
    <circle cx="424" cy="712" r="19" fill="none" stroke="var(--icon-green)" stroke-width="5"/>
    <path d="M412 720 Q414 703 434 703 Q434 720 416 720 Z" fill="var(--icon-green)"/>
    <text class="feature-caption" x="424" y="769" text-anchor="middle">LOW VOC</text>
  </g>

  <g class="feature washable">
    <rect x="569" y="713" width="40" height="14" rx="3" fill="var(--icon-blue)" transform="rotate(-10 589 720)"/>
    <path d="M578 710 V695 Q578 690 584 690 H598" fill="none" stroke="var(--icon-blue)" stroke-width="5" stroke-linecap="round"/>
    <text class="feature-caption" x="589" y="769" text-anchor="middle">WASHABLE</text>
  </g>

  <g class="feature eco-friendly">
    <circle cx="756" cy="712" r="22" fill="var(--icon-sky)"/>
    <circle cx="756" cy="712" r="22" fill="none" stroke="var(--icon-green)" stroke-width="4" stroke-dasharray="30 8"/>
    <path d="M748 718 Q750 700 766 702 Q764 718 748 718 Z" fill="var(--icon-green)"/>
    <text class="feature-caption" x="756" y="769" text-anchor="middle">ECO FRIENDLY</text>
  </g>

  <path class="volume-tab" d="M168 846 H510 Q528 846 530 828 V820 Q532 797 556 797 H620 Q644 797 646 820 V828 Q648 846 666 846 H1013 V858 H168 Z" fill="var(--ink)"/>
  <text class="volume" x="588" y="841" text-anchor="middle">20 L</text>

  <text class="tagline" x="593" y="904" text-anchor="middle" textLength="563" lengthAdjust="spacing">AN ORVESSA APPLICATION</text>
</svg>
</body>
</html>
```